Waste and recycling company seeks artwork design and branding for plastic ruler.

We require a very professional design for our marketing product 'Ruler'.
It will be on a white plastic ruler 315mm long and 39mm high.
0 – 30 on the top (in mm).
0 – 12 on the bottom (in inches).
Numbering in black (to be included as an example only) as it is already printed on the plastic stock.
3 colours. Red, Black, Harbor truck blue (colour is Pantone 3155C)
Total workable text area –
Length 312mm
Height 24mm
We would need the artwork in a vector format, either .pdf or .eps

Version 1 - Try and fit all the following info onto it.

Dot points -
• Commercial waste and recycling
• Bulk clean up bins
• Document shredding
• Liquid waste

08 7394 2816
info@quarrybins.example.au
www.quarrybins.example.au

SA Family owned and operated.

Quarry logo

With service YOU can measure
Backed by our 5 Star customer service guarantee

I would like dot points on the left side of ruler. Quarry logo in the middle of the ruler or on the far right hand side.
If Quarry logo is in the middle, then ‘with service you can measure backed by our customer service guarantee.' to the right

Version 2. If all this does not fit -
Try having no dot points and have on the left hand side
'SA Family Owned and Operated'
Underneath ‘Phone 08 7394 2816
Underneath website and email
Quarry logo

Target Market(s)

business clients

Industry/Entity Type

Recycling

Requirements
Must have
• phone number, email, logo,

```html
<!DOCTYPE html>
<html lang="en">
<head>
<meta charset="utf-8">
<title>Quarry Waste &amp; Recycling – Ruler Artwork</title>
<link rel="stylesheet" href="https://fonts.googleapis.com/css2?family=Archivo+Black&family=Arimo:ital,wght@0,400;0,700;1,400&display=swap">
<style>
  :root {
    --canvas: #e6e6e6;
    --ruler: #ffffff;
    --tick: #b9b9b9;
    --harbor-blue: #0e5c6b;
    --harbor-mid: #3f8694;
    --harbor-light: #8ab6be;
    --harbor-pale: #c6dfe3;
    --brand-red: #d8232a;
    --ink: #111111;
    --white: #ffffff;
  }
  * { margin: 0; padding: 0; box-sizing: border-box; }
  html, body { width: 1200px; height: 786px; overflow: hidden; }
  body { background: var(--canvas); position: relative; font-family: "Arimo", Arial, sans-serif; }

  .ruler {
    position: absolute;
    width: 1036px;
    height: 127px;
    background: var(--ruler);
    box-shadow: 2px 3px 3px rgba(0,0,0,.35);
  }
  .ruler--one { left: 84px; top: 110px; }
  .ruler--two { left: 81px; top: 330px; }
  .ruler--three { left: 81px; top: 554px; }

  .scale-mm, .scale-inch { position: absolute; left: 22px; right: 22px; }
  .scale-mm {
    top: 0; height: 10px;
    background:
      repeating-linear-gradient(90deg, var(--tick) 0 1px, transparent 1px 16.5px) 0 0 / 100% 10px no-repeat,
      repeating-linear-gradient(90deg, var(--tick) 0 1px, transparent 1px 3.3px) 0 0 / 100% 6px no-repeat;
  }
  .scale-inch {
    bottom: 0; height: 12px;
    background:
      repeating-linear-gradient(90deg, var(--tick) 0 1px, transparent 1px 84px) 0 100% / 100% 12px no-repeat,
      repeating-linear-gradient(90deg, var(--tick) 0 1px, transparent 1px 10.5px) 0 100% / 100% 6px no-repeat;
  }

  .message-band { position: absolute; left: 5px; top: 25px; width: 560px; height: 78px; }

  .headline {
    position: absolute; left: 29px; top: 23px;
    font-family: "Archivo Black", "Arial Black", sans-serif;
    font-size: 29px; line-height: 1; letter-spacing: .2px;
    color: var(--brand-red);
    text-shadow: 2px 2px 1px rgba(0,0,0,.55);
  }
  .guarantee {
    position: absolute; left: 29px; top: 59px;
    font-weight: 700; font-size: 18px; color: var(--white); white-space: nowrap;
  }
  .ruler--two .guarantee { font-size: 21.5px; top: 56px; left: 26px; letter-spacing: .3px; }
  .ruler--three .guarantee { left: 26px; font-size: 18.5px; }
  .contact {
    position: absolute; left: 29px; top: 85px;
    font-size: 13px; color: var(--white); white-space: nowrap; word-spacing: 1px;
  }
  .ruler--two .contact, .ruler--three .contact { left: 26px; }
  .contact .sep { margin: 0 7px; font-size: 9px; vertical-align: 2px; }

  .services { position: absolute; top: 25px; left: 560px; list-style: none; }
  .services li {
    position: relative; font-weight: 700; font-size: 12.5px; color: var(--ink);
    height: 19px; line-height: 19px; white-space: nowrap;
  }
  .services li::before {
    content: ""; position: absolute; left: -14px; top: 8px;
    width: 4px; height: 4px; background: var(--ink);
  }
  .services li:nth-child(1) { margin-left: 48px; }
  .services li:nth-child(2) { margin-left: 40px; }
  .services li:nth-child(3) { margin-left: 32px; }
  .services li:nth-child(4) { margin-left: 24px; }

  .brand { position: absolute; left: 826px; top: 38px; width: 200px; }
  .brand-name {
    display: flex; align-items: center; gap: 8px;
    margin-left: 12px;
    font-weight: 700; font-size: 21px; color: var(--ink); letter-spacing: .5px;
  }
  .brand-mark { width: 14px; height: 14px; background: var(--harbor-blue); }
  .brand-tagline {
    margin-top: 22px;
    font-style: italic; font-size: 11.5px; color: var(--harbor-blue); white-space: nowrap;
  }
</style>
</head>
<body>

<section class="ruler ruler--one">
  <div class="scale-mm"></div>
  <svg class="message-band" viewBox="0 0 560 78" aria-hidden="true">
    <polygon points="466,0 560,0 534,78 440,78" fill="#c6dfe3"/>
    <polygon points="466,0 540,0 514,78 440,78" fill="#8ab6be"/>
    <polygon points="466,0 524,0 498,78 440,78" fill="#3f8694"/>
    <polygon points="0,0 510,0 484,78 0,78" fill="#0e5c6b"/>
    <rect x="0" y="0" width="18" height="30" fill="#3f8694"/>
  </svg>
  <h1 class="headline">With service YOU can measure</h1>
  <p class="guarantee">Backed by our 5 star customer service guarantee</p>
  <p class="contact">08 7394 2816<span class="sep">■</span>info@quarrybins.example.au<span class="sep">■</span>www.quarrybins.example.au</p>
  <ul class="services">
    <li>Commercial waste and recycling</li>
    <li>Document shredding</li>
    <li>Bulk clean up bins</li>
    <li>Liquid waste</li>
  </ul>
  <div class="brand">
    <div class="brand-name"><span class="brand-mark"></span>QUARRY</div>
    <p class="brand-tagline">SA family owned and operated</p>
  </div>
  <div class="scale-inch"></div>
</section>

<section class="ruler ruler--two">
  <div class="scale-mm"></div>
  <svg class="message-band" viewBox="0 0 560 78" aria-hidden="true">
    <polygon points="466,0 560,0 534,78 440,78" fill="#c6dfe3"/>
    <polygon points="466,0 540,0 514,78 440,78" fill="#8ab6be"/>
    <polygon points="466,0 524,0 498,78 440,78" fill="#3f8694"/>
    <polygon points="0,0 510,0 484,78 0,78" fill="#0e5c6b"/>
    <rect x="0" y="0" width="18" height="30" fill="#3f8694"/>
  </svg>
  <h1 class="headline">With service YOU can measure</h1>
  <p class="guarantee">5 star customer service guarantee</p>
  <p class="contact">08 7394 2816<span class="sep">■</span>info@quarrybins.example.au<span class="sep">■</span>www.quarrybins.example.au</p>
  <ul class="services">
    <li>Commercial waste and recycling</li>
    <li>Document shredding</li>
    <li>Bulk clean up bins</li>
    <li>Liquid waste</li>
  </ul>
  <div class="brand">
    <div class="brand-name"><span class="brand-mark"></span>QUARRY</div>
    <p class="brand-tagline">SA family owned and operated</p>
  </div>
  <div class="scale-inch"></div>
</section>

<section class="ruler ruler--three">
  <div class="scale-mm"></div>
  <svg class="message-band" viewBox="0 0 560 78" aria-hidden="true">
    <polygon points="466,0 560,0 534,78 440,78" fill="#c6dfe3"/>
    <polygon points="466,0 540,0 514,78 440,78" fill="#8ab6be"/>
    <polygon points="466,0 524,0 498,78 440,78" fill="#3f8694"/>
    <polygon points="0,0 510,0 484,78 0,78" fill="#0e5c6b"/>
    <rect x="0" y="0" width="18" height="30" fill="#3f8694"/>
  </svg>
  <h1 class="headline">With service YOU can measure</h1>
  <p class="guarantee">By our 5 star customer service guarantee</p>
  <p class="contact">08 7394 2816<span class="sep">■</span>info@quarrybins.example.au<span class="sep">■</span>www.quarrybins.example.au</p>
  <ul class="services">
    <li>Commercial waste and recycling</li>
    <li>Document shredding</li>
    <li>Bulk clean up bins</li>
    <li>Liquid waste</li>
  </ul>
  <div class="brand">
    <div class="brand-name"><span class="brand-mark"></span>QUARRY</div>
    <p class="brand-tagline">SA family owned and operated</p>
  </div>
  <div class="scale-inch"></div>
</section>

</body>
</html>
```